VornaLift.com

Looking for a Graphic Designer/Web Designer to make a really modern/clean "skin" for our new Fitness website. This 'skin' will be used for the border/frame of all pages of the site.

Background:
VornaLift is a company that is solely dedicated to providing personal trainers with a all-in-one suite of services to help manager, increase, and support their clients.

For a small monthly fee, personal trainers will have the ability to manage clients, schedule sessions, take payments, provide education, monitor their progress, track their results, and more.

What we are looking for:
Someone to create the graphics/banners for the page, help with fonts, size of fonts, spacing between elements, what borders, their colors.

The main page needs to focus on allowing the user to select whether they are a 'trainer' or a client. From their the page will open up to two difference experiences.

Personal Trainer Experience:
Personal Trainer Main page will show a sales section to offer the product and services. Once a trainer signs up for our service, they will log into a dashboard that will have several icons that lead to difference functions of the site. We will need help with placement of the various fields/data to make it visually appealing and provide a friendly user experience.

The client Experience: They will be directed to a client log-in page. Once logged in, they will be provided with a similar dashboard menu that provides them various options as well. We will need help with organizing the fields/data to make it visually appealing and provide a friend user experience.

This will be a great experience for both the designer and for us. Once the "skin" is created, it's a matter of making the rest visually appealing.

The icons being used for the 'dashboard menu':
http://plimvector.example/fitness-icons-4899-vector-clipart.html

Any questions, please feel free to ask.

Target Market(s)

Our target market are personal trainers both seasoned and new.

Industry/Entity Type

Education

Requirements
Must have
• Must have a modern, upbeat look.
The main page for trainers needs to be professional and really highlight our services (selling page).
should have the option to link to the following services to see more about what you get:
Exercise, Nutrition, Supplementation, Documentation, Scheduling and Email, Payment process, Marketing
Nice to have
• Here are pages to some of the sites we liked (visually):
1. https://www.brindle.example/ (really like the look of brnidle)
2. http://odetrevalk.example/
3. http://www.suavetiles.example/gallery/pilo/
4. https://www.brindle.example/
5 https://tunegrove.example/
5. http://www.zapperly.example/
6. http://www.penrix.example/
7. http://www.limnoderm.example/
Should not have
• Here are some of our competitors:
www.trellacoach.example
www.purobench.example
www.dovecalendo.example

```html
<!DOCTYPE html>
<html lang="en">
<head>
<meta charset="utf-8">
<title>VornaLift – User Login</title>
<link href="https://fonts.googleapis.com/css2?family=Montserrat:wght@400;600;700;800&display=swap" rel="stylesheet">
<style>
  :root {
    --brand-green: #0db14b;
    --white: #ffffff;
    --field-text: #4a4a4a;
    --field-border: #d9d9d9;
    --scene-dark: #141617;
    --scene-mid: #2b2f31;
    --scene-light: #4a4f52;
  }
  * { box-sizing: border-box; margin: 0; padding: 0; }
  html, body {
    width: 1200px;
    height: 720px;
    overflow: hidden;
    background: var(--scene-dark);
    font-family: "Montserrat", Arial, sans-serif;
  }
  .login-screen {
    position: relative;
    width: 1200px;
    height: 720px;
    overflow: hidden;
  }
  .hero-backdrop {
    position: absolute;
    inset: 0;
    background:
      radial-gradient(ellipse 420px 360px at 1010px 300px, var(--scene-light) 0%, rgba(74,79,82,0) 70%),
      radial-gradient(ellipse 360px 420px at 420px 380px, #3a3532 0%, rgba(58,53,50,0) 75%),
      linear-gradient(160deg, var(--scene-mid) 0%, var(--scene-dark) 70%);
  }
  .brand-name {
    position: absolute;
    left: 483px;
    top: 192px;
    color: var(--white);
    font-size: 48px;
    font-weight: 600;
    letter-spacing: 0;
    line-height: 1;
  }
  .login-title {
    position: absolute;
    left: 454px;
    top: 282px;
    color: var(--brand-green);
    font-size: 34px;
    font-weight: 800;
    letter-spacing: -1px;
    line-height: 1;
  }
  .login-field {
    position: absolute;
    left: 456px;
    width: 288px;
    height: 38px;
    padding: 0 15px;
    border: 1px solid var(--field-border);
    background: var(--white);
    color: var(--field-text);
    font-size: 13px;
    display: flex;
    align-items: center;
  }
  .login-field--username { top: 325px; }
  .login-field--password { top: 376px; }
  .forgot-link {
    position: absolute;
    right: 458px;
    top: 421px;
    color: var(--white);
    font-size: 11px;
    font-weight: 700;
    text-decoration: none;
  }
  .login-button {
    position: absolute;
    left: 457px;
    top: 426px;
    width: 92px;
    height: 36px;
    background: var(--brand-green);
    color: var(--white);
    font-size: 16px;
    font-weight: 800;
    display: flex;
    align-items: center;
    justify-content: center;
    letter-spacing: -0.3px;
  }
  .copyright {
    position: absolute;
    left: 0;
    width: 1196px;
    top: 517px;
    text-align: center;
    color: var(--white);
    font-size: 9px;
    font-weight: 400;
  }
</style>
</head>
<body>
  <main class="login-screen">
    <div class="hero-backdrop" role="img" aria-label="Darkened gym photograph of an athlete training on a rowing machine"></div>

    <span class="brand-name">VornaLift</span>

    <h1 class="login-title">USER LOGIN</h1>

    <div class="login-field login-field--username">Username</div>
    <div class="login-field login-field--password">Password</div>

    <div class="login-button">LOGIN</div>
    <a class="forgot-link" href="#">Forgot Password?</a>

    <p class="copyright">© 2013,&nbsp; VornaLift, All Rights Reserved</p>
  </main>
</body>
</html>
```